Silverleaf Rise Accounting Program

size of ad Full: 7” x 9.6”
1- this is for a ladies program so it should appeal to women.
2-however, I do not want any pictures of people in this ad.
3-all the text should be seen and not covered over by graphics.
4-It should be an ad that will draw people's attention and people should look at it and say it looks nice I want to see that ad.
5-I have put all the instructions in yellow in the file below.
6-please leave 1 inch for the footer .
good luck with this project

• no picture or vector of people.

```html
<!DOCTYPE html>
<html lang="en">
<head>
<meta charset="utf-8">
<title>Silverleaf Rise Accounting Program</title>
<link rel="stylesheet" href="https://fonts.googleapis.com/css2?family=Ubuntu:wght@700&family=Roboto:wght@300;400&family=Bebas+Neue&family=Montserrat:ital,wght@0,700;0,800;1,800&display=swap">
<style>
  :root{
    --stage:#d4d4d4;
    --green-dark:#22603a;
    --green-mid:#3f8a46;
    --green-light:#6cbd58;
    --green-pale:#b3e38a;
    --white:#ffffff;
    --ink:#3a3f44;
    --tab:#d8e8ee;
    --orange:#ff8a2b;
    --red:#ff5a4a;
    --yellow:#fdc52e;
    --pink:#f7617f;
    --magenta:#d01459;
    --meet:#2a73e8;
    --black:#000000;
  }
  *{margin:0;padding:0;box-sizing:border-box}
  html,body{width:1200px;height:1200px;overflow:hidden;background:var(--stage)}
  .flyer{position:absolute;left:200px;top:50px;width:800px;height:1100px;overflow:hidden;color:var(--white);font-family:"Roboto",sans-serif}
  .backdrop{position:absolute;inset:0}
  .title{position:absolute;left:64px;top:28px;font-family:"Ubuntu",sans-serif;font-weight:700;font-size:48px;letter-spacing:.3px}
  .intro{position:absolute;left:61px;top:111px;height:151px;border-left:3px solid var(--white);padding-left:10px;font-size:25px;line-height:31px}
  .intro p+p{margin-top:30px}
  .duration{position:absolute;left:517px;top:60px;transform:rotate(-8deg);transform-origin:left top}
  .duration .lead{display:inline-block;margin-left:23px;background:var(--white);color:var(--ink);border-radius:14px;padding:3px 20px 2px 22px;font-family:"Montserrat",sans-serif;font-weight:700;font-size:12px}
  .duration .lead span{font-weight:400}
  .duration .main{display:block;margin-top:-4px;background:linear-gradient(90deg,var(--red),var(--orange) 40%,#ffa73a);border-radius:24px;padding:4px 20px 5px 20px;font-family:"Montserrat",sans-serif;font-style:italic;font-weight:800;font-size:32px;line-height:1.15;white-space:nowrap;box-shadow:0 4px 8px rgba(0,0,0,.2)}
  .banner-text{position:absolute;font-family:"Bebas Neue",sans-serif;white-space:nowrap;transform-origin:left bottom}
  .firms{left:358px;top:318px;color:var(--ink);font-size:21px;line-height:22px;transform:rotate(-4deg)}
  .stats{left:262px;top:392px;font-size:48px;line-height:56px;transform:rotate(-4deg)}
  .advantage{left:158px;top:565px;font-size:38px;transform:rotate(-3.5deg)}
  .meet{position:absolute;left:370px;top:656px;display:flex;align-items:center;gap:8px;font-size:15px}
  .meet .dot{width:46px;height:46px;border-radius:50%;background:var(--meet)}
  .session{position:absolute;left:0;top:710px;width:800px;text-align:center;font-size:25px;line-height:36px}
  .contact{position:absolute;left:145px;top:782px;width:473px;height:100px;border-radius:50px;background:linear-gradient(90deg,var(--yellow),var(--orange) 45%,var(--red));text-align:center;font-family:"Montserrat",sans-serif;font-style:italic;font-weight:800;font-size:26px;line-height:38px;padding-top:12px}
  .ranking{position:absolute;left:169px;top:911px;width:56px;height:56px;border-radius:50%;background:var(--orange)}
  .accolade{position:absolute;left:250px;top:905px;font-size:20px;line-height:23px}
  .note{position:absolute;left:24px;top:975px;transform:rotate(-90deg);transform-origin:left top;font-size:16px;white-space:nowrap;letter-spacing:.3px}
  .footer{position:absolute;left:0;bottom:0;width:800px;height:112px;background:var(--black);display:flex;align-items:center;justify-content:center;font-weight:300;font-size:54px}
</style>
</head>
<body>
<main class="flyer">
  <svg class="backdrop" width="800" height="1100" viewBox="0 0 800 1100" aria-hidden="true">
    <defs>
      <linearGradient id="field" x1="0" y1="0" x2="1" y2="0">
        <stop offset="0" stop-color="#66bb5a"/>
        <stop offset=".45" stop-color="#3f8a46"/>
        <stop offset="1" stop-color="#22603a"/>
      </linearGradient>
      <linearGradient id="sheen" x1="0" y1="0" x2="1" y2="1">
        <stop offset="0" stop-color="#b3e38a" stop-opacity=".9"/>
        <stop offset="1" stop-color="#6cbd58" stop-opacity="0"/>
      </linearGradient>
      <linearGradient id="paleRight" x1="0" y1="0" x2="1" y2="0">
        <stop offset="0" stop-color="#b3e38a"/>
        <stop offset="1" stop-color="#6a9a70"/>
      </linearGradient>
      <linearGradient id="orangeBand" x1="0" y1="0" x2="1" y2="0">
        <stop offset="0" stop-color="#ff5a4a"/>
        <stop offset=".6" stop-color="#ff8a2b"/>
        <stop offset="1" stop-color="#fdb62a"/>
      </linearGradient>
      <linearGradient id="pinkBand" x1="0" y1="0" x2="1" y2="0">
        <stop offset="0" stop-color="#f7617f"/>
        <stop offset=".6" stop-color="#e52e6a"/>
        <stop offset="1" stop-color="#d01459"/>
      </linearGradient>
    </defs>
    <rect width="800" height="1100" fill="url(#field)"/>
    <polygon points="0,0 160,0 0,260" fill="url(#sheen)"/>
    <polygon points="30,0 160,0 0,160 0,0" fill="#a6dc84" opacity=".5"/>
    <polygon points="485,0 800,0 800,152 720,231" fill="#6cbd58"/>
    <polygon points="600,0 800,0 800,32 720,108" fill="#b3e38a"/>
    <polygon points="0,910 135,683 270,910 270,990 0,990" fill="url(#sheen)" opacity=".8"/>
    <polygon points="0,990 135,765 340,990" fill="#a6dc84" opacity=".55"/>
    <polygon points="620,890 800,670 800,990 650,990" fill="url(#paleRight)" opacity=".9"/>
    <line x1="0" y1="385" x2="210" y2="590" stroke="#b3e38a" stroke-width="1" opacity=".6"/>
    <line x1="0" y1="735" x2="135" y2="610" stroke="#b3e38a" stroke-width="1" opacity=".6"/>
    <line x1="135" y1="610" x2="180" y2="650" stroke="#b3e38a" stroke-width="1" opacity=".6"/>
    <line x1="470" y1="95" x2="560" y2="0" stroke="#b3e38a" stroke-width="1" opacity=".6"/>
    <polygon points="275,320 578,300 578,358 275,368" fill="#d8e8ee"/>
    <polygon points="275,362 578,350 578,358 275,368" fill="#b8c8cf"/>
    <polygon points="143,505 571,483 571,628 143,655" fill="url(#pinkBand)"/>
    <polygon points="571,494 644,494 571,530" fill="#ff8a2b"/>
    <polygon points="197,375 207,375 207,530 197,535" fill="#e43a55"/>
    <polygon points="207,375 644,345 644,494 207,520" fill="url(#orangeBand)"/>
  </svg>

  <h1 class="title">Attention Women</h1>
  <section class="intro">
    <p>A Master’s Degree in Accounting</p>
    <p>A stable, lucrative career, with high-paying, full<br>/part time opportunities in Private/Public<br>companies</p>
  </section>

  <div class="duration">
    <span class="lead">MASTERS <span>IN</span></span>
    <span class="main">12 MONTHS</span>
  </div>

  <div class="banner-text firms">RELATIONSHIPS WITH<br>100’S OF FIRMS</div>
  <div class="banner-text stats">96% PLACEMENT RATE<br>6 PLACEMENT DIRECTORS</div>
  <div class="banner-text advantage">THE LRC JOB PLACEMENT ADVANTAGE</div>

  <div class="meet"><span class="dot"></span><span>Meetline</span></div>

  <div class="session">
    <p>Sunday June 14,2pm</p>
    <p>for a Meetline link / conference number /information</p>
  </div>

  <div class="contact">
    <p>HELLO@LRCCAREERS.ORG</p>
    <p>555 014 2700X 111</p>
  </div>

  <div class="ranking" role="img" aria-label="Program ranking badge"></div>
  <p class="accolade">Northbrook Crest University,<br>Masters in Accounting program,<br>received the highest possible rating in USA</p>

  <p class="note">Graduates have been placed in top companies (full/part time jobs).</p>

  <footer class="footer">1 inch blank space</footer>
</main>
</body>
</html>
```